Personal Website for DBA of my main company

I need a website created for my personal brand for one of my Vinora of my main company. This website will be about my personal passion of wine. I am a certified sommelier and want a page that shows my passions for the wine industry. It will consist of pages that have video, pictures and possibly links to my cellar. (I have uploaded a screen shot of the only page I could find from a sommelier, I do not want to copy or look anything like this page....its just an idea of what one would look like)

Target Market(s)

Small, mostly word of mouth customers

Industry/Entity Type

Wine and Service Industry

Coding

Coded - Design and coding required

Number of Pages Required

4 page

Font styles to use
Other font styles liked:
• Font that is current but will be relevant in the future as well

Colors
0054AA
0677BA
7BADD7
CADEEF
E8F1F8
0094D4
00A9DD
6FCCEA
C7EBF8
E9F6FB
00AB8E
00BBA5
67D7C9
C6EFE9
E9F9F6
EB3D1F
EC4F4E
F09395
F8D3D4
FCEDEE

Requirements
Must have
• Landing page, video page and images page.

```html
<!DOCTYPE html>
<html lang="en">
<head>
<meta charset="utf-8">
<title>Vinora — Sommelier</title>
<link rel="stylesheet" href="https://fonts.googleapis.com/css2?family=Cormorant+Garamond:wght@500;600&family=Epilogue:wght@400;500;600&display=swap">
<style>
  :root {
    --wine: #8c1a1a;
    --wine-deep: #6a0707;
    --band-red: #6b0a0a;
    --charcoal: #2a2828;
    --footer: #4a4848;
    --bronze: #b07e5c;
    --ink: #1f1f1f;
    --muted: #8a8a8a;
    --white: #ffffff;
    --serif: "Cormorant Garamond", Georgia, serif;
    --sans: "Epilogue", Arial, sans-serif;
  }
  * { box-sizing: border-box; margin: 0; padding: 0; }
  html, body { width: 1200px; height: 3582px; overflow: hidden; }
  body { position: relative; background: var(--white); font-family: var(--sans); color: var(--ink); }
  .abs { position: absolute; }

  /* Hero */
  .hero { left: 0; top: 0; width: 1200px; height: 541px;
    background: linear-gradient(160deg, #5b4638 0%, #3c3530 45%, #5a4f4a 70%, #2e2a28 100%); }
  .hero-shade { inset: 0; background: rgba(0,0,0,.25); }
  .brand { left: 90px; top: 42px; font-family: var(--serif); font-size: 36px; font-weight: 600; color: var(--white); }
  .nav a { position: absolute; top: 50px; font-family: var(--sans); font-size: 17px; color: var(--white); text-decoration: none; }
  .btn-book { left: 920px; top: 37px; width: 202px; height: 41px; border: 1.5px solid var(--white); border-radius: 21px;
    color: var(--white); font-size: 13px; font-weight: 600; letter-spacing: .3px; display: flex; align-items: center; justify-content: center; }
  .hero-title { left: 250px; top: 228px; width: 700px; text-align: center; font-family: var(--serif); font-size: 42px; font-weight: 500; line-height: 49px; color: var(--white); }
  .hero-sub { left: 250px; top: 356px; width: 700px; text-align: center; font-size: 20px; line-height: 28px; color: var(--white); }
  .arrow { width: 48px; height: 48px; border-radius: 50%; background: var(--white); display: flex; align-items: center; justify-content: center; }

  /* Services */
  .services { left: 0; top: 541px; width: 1200px; height: 644px; background: linear-gradient(180deg, var(--wine) 0%, var(--wine-deep) 100%); }
  .section-title { width: 1200px; left: 0; text-align: center; font-family: var(--serif); font-size: 29px; font-weight: 500; letter-spacing: 1px; }
  .services .section-title { top: 110px; color: var(--white); }
  .rule { height: 1.5px; background: var(--white); }
  .service { color: var(--white); }
  .service .num { position: absolute; left: 0; top: 0; font-family: var(--serif); font-size: 30px; font-weight: 600; }
  .service h3 { position: absolute; font-family: var(--serif); font-size: 16px; font-weight: 500; white-space: nowrap; }
  .service p { position: absolute; font-size: 12px; line-height: 19px; }
  .leaf { left: 0; top: 445px; width: 34px; height: 60px; background: rgba(255,255,255,.35); border-radius: 0 30px 30px 0; }

  /* Quote */
  .quote { left: 0; top: 1185px; width: 1200px; height: 308px; background: radial-gradient(ellipse at 55% 50%, #3a3636 0%, var(--charcoal) 70%); }
  .quote p { position: absolute; left: 0; top: 132px; width: 1200px; text-align: center; font-family: var(--serif); font-size: 38px; color: var(--white); }

  /* About */
  .grape-left { left: 0; top: 1790px; width: 260px; height: 240px; border-radius: 50%; background: radial-gradient(circle, #e3e3e3 0%, rgba(227,227,227,0) 70%); }
  .grape-right { left: 1040px; top: 1590px; width: 220px; height: 360px; border-radius: 50%; background: radial-gradient(circle, #e3e3e3 0%, rgba(227,227,227,0) 70%); }
  .photo-main { left: 154px; top: 1573px; width: 291px; height: 388px; background: linear-gradient(135deg, #8a5a3e, #3b5790 55%, #6f7d6a); }
  .photo-side { left: 332px; top: 1744px; width: 194px; height: 260px; background: linear-gradient(160deg, #b9865f, #2c2a2a 55%, #b5242c); border: 2px solid var(--white); }
  .about-title { left: 628px; top: 1596px; font-family: var(--serif); font-size: 34px; font-weight: 500; color: var(--bronze); }
  .about-rule { left: 628px; top: 1640px; width: 40px; height: 1.5px; background: var(--bronze); }
  .about-text { left: 626px; width: 380px; font-size: 14px; line-height: 20px; color: var(--ink); }
  .btn-outline { border: 1.5px solid var(--ink); border-radius: 21px; display: flex; align-items: center; justify-content: center; font-size: 14px; color: var(--ink); }

  /* Contact band */
  .contact-band { left: 2px; top: 2098px; width: 1198px; height: 153px; background: var(--band-red); }
  .contact-band h2 { position: absolute; left: 330px; top: 52px; font-family: var(--serif); font-size: 40px; font-weight: 500; color: var(--white); white-space: nowrap; }
  .contact-band .btn-outline { position: absolute; left: 736px; top: 57px; width: 134px; height: 40px; border-color: var(--white); color: var(--white); font-size: 13px; }

  /* Gallery */
  .gallery-tile { top: 2251px; height: 320px; }

  /* Blog */
  .blog-title { top: 2675px; color: var(--bronze); }
  .blog-img { top: 2752px; width: 223px; height: 142px; }
  .blog-card h4 { position: absolute; font-family: var(--serif); font-size: 16px; font-weight: 500; color: var(--ink); white-space: nowrap; }
  .blog-card p { position: absolute; width: 215px; font-size: 13px; line-height: 22px; color: var(--muted); }

  .divider { left: 89px; top: 3124px; width: 1035px; border-top: 1.5px dashed #a8a8a8; }

  /* Newsletter */
  .newsletter-title { left: 0; top: 3176px; width: 1290px; text-align: center; font-family: var(--serif); font-size: 38px; font-weight: 500; color: var(--ink); }
  .field { border-bottom: 1.5px solid #444; font-size: 13px; color: var(--ink); padding-bottom: 14px; width: 239px; }
  .btn-news { left: 809px; top: 3280px; width: 134px; height: 39px; border-color: var(--bronze); color: var(--bronze); font-size: 13px; }

  /* Footer */
  .footer { left: 0; top: 3400px; width: 1200px; height: 182px; background: var(--footer); }
  .footer a { position: absolute; top: 45px; font-family: var(--serif); font-size: 16px; color: var(--white); text-decoration: none; }
  .social { position: absolute; top: 93px; width: 24px; height: 24px; border-radius: 50%; border: 2px solid var(--white); }
  .copyright { position: absolute; left: 0; top: 154px; width: 1200px; text-align: center; font-size: 13px; color: var(--white); }
</style>
</head>
<body>

<header class="abs hero" role="img" aria-label="Photo of the sommelier holding a wine bottle and glass in a restaurant">
  <div class="abs hero-shade"></div>
</header>
<div class="abs brand">Vinora</div>
<nav class="nav">
  <a style="left:510px">Home</a>
  <a style="left:603px">About</a>
  <a style="left:703px">Services</a>
  <a style="left:826px">Blog</a>
</nav>
<div class="abs btn-book">BOOK A WINE TESTING</div>
<h1 class="abs hero-title">Tastings, corporate events and private winery tours</h1>
<p class="abs hero-sub">Lorem ipsum dolor sit amet, consectetur adipiscing elit. Nisl, non suspendisse suspendisse nulla vulputate id pellentesque.</p>
<div class="abs arrow" style="left:90px;top:267px">
  <svg width="22" height="22" viewBox="0 0 22 22" fill="none" stroke="#222" stroke-width="2" stroke-linecap="round" stroke-linejoin="round"><path d="M18 11H4M10 5l-6 6 6 6"/></svg>
</div>
<div class="abs arrow" style="left:1084px;top:243px">
  <svg width="22" height="22" viewBox="0 0 22 22" fill="none" stroke="#222" stroke-width="2" stroke-linecap="round" stroke-linejoin="round"><path d="M4 11h14M12 5l6 6-6 6"/></svg>
</div>

<section class="abs services">
  <h2 class="abs section-title">OUR SERVICES</h2>
  <div class="abs rule" style="left:587px;top:167px;width:117px"></div>
  <div class="abs leaf" role="img" aria-label="Faint vine leaf decoration"></div>

  <div class="abs service" style="left:100px;top:212px">
    <span class="num">01</span>
    <h3 style="left:45px;top:10px">Private Dinners / Sommelier</h3>
    <p style="left:45px;top:40px;width:270px">Lorem ipsum dolor sit amet, consectetur adipiscing elit. Quis malesuada massa nisi, eleifend. Tortor neque, sollicitudin sit aliquam ac.</p>
  </div>
  <div class="abs service" style="left:452px;top:212px">
    <span class="num">02</span>
    <h3 style="left:48px;top:5px">Wine Conslutation</h3>
    <p style="left:48px;top:31px;width:250px">Lorem ipsum dolor sit amet, consectetur adipiscing elit. Quis malesuada massa nisi, eleifend. Tortor neque, sollicitudin sit aliquam ac.</p>
  </div>
  <div class="abs service" style="left:810px;top:218px">
    <span class="num">03</span>
    <h3 style="left:48px;top:5px">Monthly Maintenance</h3>
    <p style="left:48px;top:31px;width:250px">Lorem ipsum dolor sit amet, consectetur adipiscing elit. Quis malesuada massa nisi, eleifend. Tortor neque, sollicitudin sit aliquam ac.</p>
  </div>
  <div class="abs service" style="left:268px;top:389px">
    <span class="num">04</span>
    <h3 style="left:52px;top:6px">Sell Your Cellar</h3>
    <p style="left:52px;top:35px;width:232px">Lorem ipsum dolor sit amet, consectetur adipiscing elit. Quis malesuada massa nisi, eleifend. Tortor neque, sollicitudin sit aliquam ac.</p>
  </div>
  <div class="abs service" style="left:633px;top:386px">
    <span class="num">05</span>
    <h3 style="left:50px;top:5px">Wine Testing</h3>
    <p style="left:50px;top:34px;width:232px">Lorem ipsum dolor sit amet, consectetur adipiscing elit. Quis malesuada massa nisi, eleifend. Tortor neque, sollicitudin sit aliquam ac.</p>
  </div>
</section>

<section class="abs quote" role="img" aria-label="Red wine being poured into a glass on a dark background">
  <p>“ Everyone Likes Wine”</p>
</section>

<section class="about">
  <div class="abs grape-left" role="img" aria-label="Faint grape bunch sketch"></div>
  <div class="abs grape-right" role="img" aria-label="Faint grape leaf and bunch sketch"></div>
  <div class="abs photo-main" role="img" aria-label="Sommelier in a blue blazer leaning against a wall with a wine bottle"></div>
  <div class="abs photo-side" role="img" aria-label="Sommelier holding a red wine bag"></div>
  <h2 class="abs about-title">About me</h2>
  <div class="abs about-rule"></div>
  <p class="abs about-text" style="top:1658px">Lorem ipsum dolor sit amet, consectetur adipiscing elit. Eu at ut felis mi lacus. Amet, vestibulum in euismod massa erat orci. Vitae congue turpis.</p>
  <p class="abs about-text" style="top:1743px;left:628px">Lorem ipsum dolor sit amet, consectetur adipiscing elit. Eu at ut felis mi lacus. Amet, vestibulum in euismod massa erat orci. Vitae congue turpis.</p>
  <div class="abs btn-outline" style="left:628px;top:1834px;width:186px;height:40px">Read more about me</div>
</section>

<section class="abs contact-band">
  <h2>Get in touch with me</h2>
  <div class="btn-outline">Contact Me</div>
</section>

<div class="abs gallery-tile" style="left:0;width:285px;background:linear-gradient(150deg,#3b3b3b,#1c1c1c 60%,#3a0c12)" role="img" aria-label="Red wine poured into a glass"></div>
<div class="abs gallery-tile" style="left:285px;width:309px;background:linear-gradient(170deg,#2a1d15,#5a3b24 55%,#8a5a30)" role="img" aria-label="Wine bottle and glass of white wine on a bar"></div>
<div class="abs gallery-tile" style="left:594px;width:310px;background:linear-gradient(170deg,#6a5040,#8c7a6a 50%,#d8d2cc)" role="img" aria-label="Friends tasting wine together in a kitchen"></div>
<div class="abs gallery-tile" style="left:904px;width:296px;background:linear-gradient(160deg,#c6c0b4,#4b5a3a 50%,#3a1010)" role="img" aria-label="Hand holding a glass of red wine near bottles"></div>

<section class="blog">
  <h2 class="abs section-title blog-title">LATEST BLOG</h2>
  <div class="blog-card">
    <div class="abs blog-img" style="left:211px;background:linear-gradient(150deg,#5a2a1a,#2a1a16 50%,#c8c0b8)" role="img" aria-label="Glass of red wine held beside bottles"></div>
    <h4 style="left:211px;top:2912px">The 5 Best Wineries to Visit</h4>
    <p style="left:212px;top:2941px">Lorem ipsum dolor sit amet, consectetur adipiscing elit. In massa semper urna, ultrices sapien, odio. Vivamus.</p>
  </div>
  <div class="blog-card">
    <div class="abs blog-img" style="left:487px;background:linear-gradient(150deg,#8fa070,#c9b8a0 50%,#5a6a4a)" role="img" aria-label="People chatting with wine at an outdoor gathering"></div>
    <h4 style="left:487px;top:2912px">The 5 Best Wineries to Visit</h4>
    <p style="left:488px;top:2941px">Lorem ipsum dolor sit amet, consectetur adipiscing elit. In massa semper urna, ultrices sapien, odio. Vivamus.</p>
  </div>
  <div class="blog-card">
    <div class="abs blog-img" style="left:763px;background:linear-gradient(150deg,#3a3a36,#6a4a3a 50%,#b7a58a)" role="img" aria-label="Guests toasting with glasses of red wine"></div>
    <h4 style="left:763px;top:2912px">The 5 Best Wineries to Visit</h4>
    <p style="left:764px;top:2941px">Lorem ipsum dolor sit amet, consectetur adipiscing elit. In massa semper urna, ultrices sapien, odio. Vivamus.</p>
  </div>
</section>

<div class="abs divider"></div>

<section class="newsletter">
  <h2 class="abs newsletter-title">Join Our Newsletter</h2>
  <div class="abs field" style="left:256px;top:3288px">Your name</div>
  <div class="abs field" style="left:540px;top:3283px;padding-left:17px">Email</div>
  <div class="abs btn-outline btn-news">Contact Me</div>
</section>

<footer class="abs footer">
  <a style="left:465px">About</a>
  <a style="left:537px">Services</a>
  <a style="left:620px">Contact</a>
  <a style="left:706px">Blog</a>
  <span class="social" style="left:546px" aria-label="Social link"></span>
  <span class="social" style="left:588px" aria-label="Social link"></span>
  <span class="social" style="left:630px" aria-label="Social link"></span>
  <p class="copyright">© 2022. All Rights Reserved.</p>
</footer>

</body>
</html>
```